KVAP Property Flyer - For Support Coordinators

Revamping our current brochures and social media posts for our properties. We need a clearer, simpler design that would be designed for Support Coordinators. Attached is our current brochure for reference.

Key details to highlight would include:
- Type of property: Studio Apartments with Psychosocial Disability Support located in Inner West
- Accommodation features
- Services

Our logo is also attached, please make the brochure with similar branding colours and fonts.

Designs look the same

Sick

Font styles to use
Sans Serif
Other font styles liked:
• Montserrat Light and Montserrat Semi Bold

Colors
0054AA
0677BA
7BADD7
CADEEF
E8F1F8

Requirements
Nice to have
• Please refer to this style guide: https://slides.trovelmark.com/deck/8TkwPzLmRd5VbQx2NcYh4GfJs7AeUo9WiKnBrMp3tZq/view?mode=shared

```html
<!DOCTYPE html>
<html lang="en">
<head>
<meta charset="utf-8">
<title>Kindred Haven – Brochure Design Option A</title>
<link href="https://fonts.googleapis.com/css2?family=Montserrat:wght@300;400;500&display=swap" rel="stylesheet">
<style>
  :root {
    --board: #58585a;
    --sheet: #c8c8c9;
    --ink: #1d1d1f;
    --blue: #2a9bd8;
    --blue-deep: #0f6fa8;
    --blue-mid: #1e8fd0;
    --white: #ffffff;
    --caption: #6a6a6a;
    --rule: #5a5a5c;
  }
  * { box-sizing: border-box; margin: 0; padding: 0; }
  html, body { width: 1200px; height: 849px; overflow: hidden; }
  body { background: var(--board); font-family: 'Montserrat', sans-serif; color: var(--ink); position: relative; }

  .board-label { position: absolute; color: var(--white); font-weight: 500; font-size: 14px; letter-spacing: 3px; }
  .board-label--back { left: 78px; top: 30px; }
  .board-label--front { right: 76px; top: 30px; }
  .board-label--option { left: 76px; top: 809px; }

  .sheet { position: absolute; left: 74px; top: 52px; width: 1052px; height: 744px; background: var(--sheet); overflow: hidden; }
  .sheet-shapes { position: absolute; inset: 0; width: 100%; height: 100%; }

  .brand { position: absolute; display: flex; align-items: center; gap: 10px; }
  .brand-dot { width: 30px; height: 30px; border-radius: 50%; background: var(--blue); }
  .brand-name { font-weight: 400; font-size: 21px; line-height: 19px; letter-spacing: 1px; color: var(--ink); }
  .brand--back { left: 334px; top: 47px; }
  .brand--front { left: 823px; top: 47px; }

  .welcome { position: absolute; left: 71px; top: 128px; width: 340px; }
  .welcome-kicker { font-weight: 300; font-size: 19px; line-height: 20px; }
  .welcome-place { font-weight: 300; font-size: 41px; line-height: 40px; color: var(--blue); letter-spacing: .5px; }
  .welcome-body { font-weight: 500; font-size: 7.8px; line-height: 10.6px; margin-top: 4px; }
  .welcome-body + .welcome-body { margin-top: 3px; }

  .kitchen-caption { position: absolute; left: 570px; top: 279px; color: var(--white); font-weight: 300; font-size: 19px; line-height: 21px; letter-spacing: .5px; }

  .units-title { position: absolute; right: 58px; top: 326px; font-weight: 300; font-size: 19px; }
  .unit-grid { position: absolute; left: 570px; top: 353px; width: 438px; height: 259px; display: grid; grid-template-columns: 225px 213px; grid-template-rows: 131px 128px; border-radius: 0 22px 22px 0; overflow: hidden; }
  .unit { position: relative; background: linear-gradient(135deg, #eef0f1 0%, #d5d9db 45%, #9aa0a4 100%); }
  .unit:nth-child(2) { background: linear-gradient(135deg, #8d9296 0%, #e6e8e9 45%, #c9cdd0 100%); }
  .unit:nth-child(3) { background: linear-gradient(135deg, #cfd3d5 0%, #f1f2f3 50%, #6f7376 100%); }
  .unit:nth-child(4) { background: linear-gradient(180deg, #eceeef 0%, #9fc3dc 40%, #a86a52 75%, #e8e9ea 100%); }
  .unit-label { position: absolute; left: 2px; bottom: 6px; padding: 1px 8px 1px 3px; border-radius: 0 10px 10px 0; background: rgba(255,255,255,.55); color: var(--caption); font-weight: 300; font-size: 12.5px; }

  .section-title { position: absolute; left: 60px; font-weight: 300; font-size: 23px; letter-spacing: .3px; }
  .section-title--communities { top: 520px; }
  .section-title--features { top: 613px; left: 61px; }
  .section-rule { position: absolute; left: 60px; top: 605px; width: 405px; height: 1px; background: var(--rule); }

  .perk { position: absolute; display: flex; align-items: center; gap: 6px; }
  .perk-icon { width: 27px; height: 27px; background: var(--blue); border-radius: 2px; display: flex; align-items: center; justify-content: center; flex-shrink: 0; }
  .perk-icon svg { width: 19px; height: 19px; }
  .perk-text { font-weight: 500; font-size: 7.4px; line-height: 10.6px; white-space: nowrap; }

  .emergency { position: absolute; left: 586px; top: 635px; }
  .emergency-title { font-weight: 300; font-size: 19px; letter-spacing: .5px; margin-bottom: 2px; }
  .emergency-line { font-weight: 400; font-size: 7.8px; line-height: 10.6px; }
</style>
</head>
<body>
  <div class="board-label board-label--back">Back Side</div>
  <div class="board-label board-label--front">Front Side</div>
  <div class="board-label board-label--option">Brochure Design Option _A</div>

  <section class="sheet">
    <svg class="sheet-shapes" viewBox="0 0 2013 1423" preserveAspectRatio="none">
      <defs>
        <linearGradient id="bathTone" x1="0" y1="0" x2="1" y2="1">
          <stop offset="0" stop-color="#6f7e82"/>
          <stop offset=".3" stop-color="#e9ebec"/>
          <stop offset=".7" stop-color="#f4f5f5"/>
          <stop offset="1" stop-color="#8b8e92"/>
        </linearGradient>
        <linearGradient id="kitchenTone" x1="0" y1="0" x2="1" y2="1">
          <stop offset="0" stop-color="#1e8fd0"/>
          <stop offset=".55" stop-color="#1a82c0"/>
          <stop offset="1" stop-color="#0f6fa8"/>
        </linearGradient>
      </defs>
      <g role="img" aria-label="Photo of a bright studio bathroom with shower, toilet and vanity">
        <path d="M0,530 L780,530 C880,530 920,430 1007,270 L1007,637 L849,637 C700,650 620,945 419,945 L0,945 Z" fill="url(#bathTone)"/>
      </g>
      <g role="img" aria-label="Blue-tinted photo of the studio kitchenette and bathroom">
        <path d="M1007,270 C1060,220 1100,205 1160,205 L1870,200 C1950,200 1990,100 2013,40 L2013,290 C1900,300 1860,420 1780,520 C1720,600 1620,637 1500,637 L1007,637 Z" fill="url(#kitchenTone)"/>
      </g>
    </svg>

    <div class="brand brand--back">
      <span class="brand-dot"></span>
      <span class="brand-name">KINDRED<br>HAVEN</span>
    </div>
    <div class="brand brand--front">
      <span class="brand-dot"></span>
      <span class="brand-name">KINDRED<br>HAVEN</span>
    </div>

    <div class="welcome">
      <p class="welcome-kicker">Welcome to</p>
      <h1 class="welcome-place">Harbourvale</h1>
      <p class="welcome-body">Located in the heart of Harbourvale, our new 20 self-contained studio apartments which have a kitchen with fridge, small stove top and microwave. It has a single bed, tv, dining table and bathroom. Some apartments have small balconies, and some have decks overlooking the bustling suburb.</p>
      <p class="welcome-body">Situated a 5 minute walk to Harbourvale Train Station, and other public transport.</p>
    </div>

    <p class="kitchen-caption">Standard<br>Kitchen Bathroom</p>

    <h2 class="units-title">Unit Images</h2>
    <div class="unit-grid">
      <div class="unit" role="img" aria-label="Photo of Single Studio A with bed and balcony"><span class="unit-label">Single Studio A</span></div>
      <div class="unit" role="img" aria-label="Photo of Single Studio B with kitchenette and dining table"><span class="unit-label">Single Studio B</span></div>
      <div class="unit" role="img" aria-label="Photo of Single Studio C with bed and kitchenette"><span class="unit-label">Single Studio C</span></div>
      <div class="unit" role="img" aria-label="Photo of Single Studio D with window view of the suburb"><span class="unit-label">Single Studio D</span></div>
    </div>

    <h2 class="section-title section-title--communities">Communities &amp; Facilities</h2>
    <div class="perk" style="left:59px;top:554px">
      <span class="perk-icon"><svg viewBox="0 0 20 20" fill="none" stroke="#fff" stroke-width="1.6" stroke-linecap="round"><path d="M5 2v6M3 2v4a2 2 0 0 0 4 0V2M5 8v10M14 2c-2 1-3 4-3 7h3v9"/></svg></span>
      <span class="perk-text">Close to shops, cafes<br>and public transport.</span>
    </div>
    <div class="perk" style="left:185px;top:554px">
      <span class="perk-icon"><svg viewBox="0 0 20 20" fill="none" stroke="#fff" stroke-width="1.4"><circle cx="10" cy="10" r="7"/><circle cx="10" cy="10" r="4"/><circle cx="10" cy="10" r="1"/><path d="M10 10l7-7"/></svg></span>
      <span class="perk-text">Local GP Practice<br>and Dentistry</span>
    </div>
    <div class="perk" style="left:298px;top:554px">
      <span class="perk-icon"><svg viewBox="0 0 20 20" fill="none" stroke="#fff" stroke-width="1.4" stroke-linejoin="round"><path d="M10 17S2 12 2 7a4 4 0 0 1 8-1 4 4 0 0 1 8 1c0 5-8 10-8 10z"/><path d="M4 10h3l1.5-2 2 4 1.5-2h4"/></svg></span>
      <span class="perk-text">Commercial Space<br>for Social Enterprise.</span>
    </div>

    <div class="section-rule"></div>

    <h2 class="section-title section-title--features">Features &amp; Services</h2>
    <div class="perk" style="left:60px;top:646px;gap:10px">
      <span class="perk-icon"><svg viewBox="0 0 20 20" fill="none" stroke="#fff" stroke-width="1.5"><rect x="3" y="3" width="14" height="12"/><path d="M6 17h8"/></svg></span>
      <span class="perk-text">24x7 Video-Intercom<br>&amp; on site support.</span>
    </div>
    <div class="perk" style="left:191px;top:646px;gap:10px">
      <span class="perk-icon"><svg viewBox="0 0 20 20" fill="none" stroke="#fff" stroke-width="1.5" stroke-linecap="round"><circle cx="10" cy="3.5" r="1.5" fill="#fff"/><path d="M10 6v5h4l2 4M8 9a4.5 4.5 0 1 0 5 6"/></svg></span>
      <span class="perk-text">Disability access<br>walkways &amp; bathroom.</span>
    </div>
    <div class="perk" style="left:326px;top:646px;gap:5px">
      <span class="perk-icon"><svg viewBox="0 0 20 20" fill="none" stroke="#fff" stroke-width="1.4" stroke-linecap="round"><path d="M3 16l5-9 3 5M9 16l5-9 3 5M2 11h8M8 11h9"/></svg></span>
      <span class="perk-text">Trained &amp; experience Staff<br>in psychosocial disability.</span>
    </div>

    <div class="emergency">
      <h2 class="emergency-title">EMERGENCY CONTACT LIST</h2>
      <p class="emergency-line">NATIONAL EMERGENCY LINE: 555 | HARBOURVALE POLICE STATION: (02) 5550 0142 | Open 24 hrs</p>
      <p class="emergency-line">HARBOURVALE FAMILY MEDICAL CENTRE: (02) 5550 0187 | Mon - Fri | 9am - 9pm | Sat - Sun | 9am - 1pm</p>
      <p class="emergency-line">WESTBROOK COUNCIL: (02) 5550 0123 | Open Mon - Fri | 8.30am - 5pm</p>
      <p class="emergency-line">ST ALDEN GENERAL HOSPITAL : (02) 5550 0166 | Open 24 hrs</p>
      <p class="emergency-line">CASSORA: (1300) 555 014 | Open Mon - Fri | 9am - 5.30pm</p>
    </div>
  </section>
</body>
</html>
```